Print on top the name of the company: (Or Similar)
Larkmoor Cleaning & Disinfecting
Because your standards aren't standard.

We adhere to ALL NVB guidelines for both residential and commercial cleaning.

Infection Control is our ultimate goal.

Instructions:
Opening a residential and commercial cleaning and disinfecting company in south Florida.

Targeting high-end residential clients, commercial and healthcare facilities, specializing in Ambulatory Care Guidelines. With a concentration and expertise in targeting Covid 19 and other transmissible pathogens.

UMRE trained.
Owned and operated by a licensed BSN Registered Nurse specially ​trained in Infection Control Prevention with over 25 years experience. Over two decades in Ambulatory Surgery Center Administration, Director of Nursing and Infection Control Prevention ad Consulting.

Looking to create a business flier that emphasizes Cleaning & Disinfection
along with the standard expectation for residential and Commercial cleaning services
Updates

Need extra days to review

Target Market(s)

Residential & Commercial

Font styles to use
Decorative

Requirements
Must have
• A checklist for cleaning services

```html
<!DOCTYPE html>
<html lang="en">
<head>
<meta charset="utf-8">
<title>Larkmoor Cleaning &amp; Disinfecting – Flyer</title>
<link rel="stylesheet" href="https://fonts.googleapis.com/css2?family=Barlow+Condensed:wght@400;600;700&family=Poppins:wght@400;500;600;700&display=swap">
<style>
  :root {
    --backdrop: #444444;
    --navy: #1f2566;
    --navy-deep: #1a1f58;
    --olive: #c5be00;
    --yellow: #f3e600;
    --yellow-dark: #a49d00;
    --white: #ffffff;
    --ink: #151515;
    --photo-light: #e9ecef;
    --photo-mid: #b9c0c6;
  }
  * { box-sizing: border-box; margin: 0; padding: 0; }
  html, body { width: 1200px; height: 1000px; overflow: hidden; }
  body { background: var(--backdrop); font-family: "Poppins", sans-serif; position: relative; }

  .flyer {
    position: absolute; left: 113px; top: 117px;
    width: 977px; height: 767px;
    background: var(--white); overflow: hidden;
  }
  .flyer-shapes { position: absolute; inset: 0; }

  .headline { position: absolute; left: 54px; top: 28px; font-family: "Barlow Condensed", sans-serif; line-height: 1; }
  .headline-top { color: var(--olive); font-weight: 600; font-size: 55px; letter-spacing: 0.2px; }
  .headline-main { color: var(--navy); font-weight: 700; font-size: 92px; margin-top: -4px; letter-spacing: 0.5px; }
  .tagline { color: var(--ink); font-weight: 400; font-size: 30px; margin-top: 6px; letter-spacing: 0.3px; }

  .service-list { position: absolute; top: 496px; }
  .service-list--commercial { left: 55px; }
  .service-list--residential { left: 342px; }
  .service-title { color: var(--yellow); font-weight: 700; font-size: 27px; line-height: 34px; margin-bottom: 18px; }
  .service-list ul { list-style: none; }
  .service-list li { display: flex; align-items: center; height: 25px; color: var(--white); font-size: 14.5px; font-weight: 400; }
  .tick { width: 16px; height: 16px; margin-left: 8px; margin-right: 15px; flex: none; }
  .service-list--residential .tick { margin-right: 18px; }

  .column-divider { position: absolute; left: 311px; top: 498px; height: 245px; border-left: 2px dotted var(--yellow); }

  .info-panel { position: absolute; left: 639px; top: 452px; width: 310px; }
  .info-note { color: var(--white); font-size: 10.5px; line-height: 13px; }
  .info-goal { color: var(--white); font-weight: 700; font-size: 14px; margin-top: 4px; }
  .credential { display: flex; align-items: center; margin-top: 12px; }
  .credential-pill { background: var(--navy); color: var(--white); font-weight: 600; font-size: 12.5px; padding: 2px 12px 2px 8px; border-radius: 0 12px 12px 0; }
  .credential-rule { flex: 1; height: 2px; background: var(--navy); margin-right: 22px; }
  .info-bio { color: var(--ink); font-size: 9.6px; line-height: 13px; margin-top: 8px; width: 300px; }
  .call-out { display: inline-block; margin-top: 16px; background: var(--navy); color: var(--white); font-weight: 700; font-size: 12px; line-height: 14px; padding: 5px 14px; border-radius: 0 20px 20px 0; width: 256px; }
  .phone { display: flex; align-items: center; margin-top: 13px; }
  .phone-icon { width: 34px; height: 34px; margin-right: 10px; }
  .phone-number { color: var(--ink); font-weight: 700; font-size: 35px; letter-spacing: 0.5px; }
</style>
</head>
<body>
<main class="flyer">
  <svg class="flyer-shapes" width="977" height="767" viewBox="0 0 977 767">
    <defs>
      <linearGradient id="photoTone" x1="0" y1="0" x2="1" y2="1">
        <stop offset="0" stop-color="#f4f5f6"/>
        <stop offset="0.6" stop-color="#d4d8dc"/>
        <stop offset="1" stop-color="#8d9196"/>
      </linearGradient>
      <linearGradient id="panelTone" x1="0" y1="0" x2="0" y2="1">
        <stop offset="0" stop-color="#a8a100"/>
        <stop offset="0.55" stop-color="#d6cd00"/>
        <stop offset="1" stop-color="#fbed00"/>
      </linearGradient>
      <linearGradient id="officeTone" x1="0" y1="0" x2="0" y2="1">
        <stop offset="0" stop-color="#cfe0ee"/>
        <stop offset="0.6" stop-color="#6f8398"/>
        <stop offset="1" stop-color="#9a9fa3"/>
      </linearGradient>
      <linearGradient id="houseTone" x1="0" y1="0" x2="0" y2="1">
        <stop offset="0" stop-color="#c9dcec"/>
        <stop offset="0.5" stop-color="#8a6a4e"/>
        <stop offset="1" stop-color="#b8b2aa"/>
      </linearGradient>
    </defs>

    <rect x="527" y="0" width="450" height="380" fill="url(#photoTone)" role="img" aria-label="Photo: technician in protective suit and respirator spraying disinfectant in a tiled room"/>

    <path d="M0 430 C120 395 300 375 470 385 C540 389 580 395 603 400 L977 360 L977 767 L0 767 Z" fill="var(--navy)"/>

    <path d="M520 355 C650 400 820 360 977 250 L977 290 C820 395 650 420 540 372 Z" fill="var(--white)"/>
    <path d="M540 372 C650 420 820 395 977 290 L977 739 L623 739 Q603 739 603 719 L603 392 Z" fill="url(#panelTone)"/>
    <path d="M560 340 C680 380 830 340 977 235 L977 252 C830 360 680 398 545 352 Z" fill="var(--olive)"/>

    <circle cx="157" cy="361" r="124" fill="none" stroke="var(--olive)" stroke-width="9" stroke-dasharray="300 480" transform="rotate(150 157 361)"/>
    <circle cx="157" cy="361" r="114" fill="var(--white)"/>
    <circle cx="157" cy="361" r="106" fill="url(#officeTone)" role="img" aria-label="Photo: modern glass office buildings along a paved street"/>

    <circle cx="427" cy="345" r="124" fill="none" stroke="var(--olive)" stroke-width="9" stroke-dasharray="300 480" transform="rotate(-30 427 345)"/>
    <circle cx="427" cy="345" r="114" fill="var(--white)"/>
    <circle cx="427" cy="345" r="106" fill="url(#houseTone)" role="img" aria-label="Photo: contemporary two-storey house with wooden facade"/>
  </svg>

  <header class="headline">
    <h1>
      <div class="headline-top">LARKMOOR CLEANING &amp;</div>
      <div class="headline-main">DISINFECTING</div>
    </h1>
    <p class="tagline">BECAUSE YOUR STANDARDS AREN'T STANDARD.</p>
  </header>

  <section class="service-list service-list--commercial">
    <h2 class="service-title">COMMERCIAL</h2>
    <ul>
      <li><svg class="tick" viewBox="0 0 16 16"><circle cx="8" cy="8" r="8" fill="#f3e600"/><path d="M4.5 8.2l2.4 2.3 4.6-4.7" fill="none" stroke="#1f2566" stroke-width="1.8"/></svg>Janitorial</li>
      <li><svg class="tick" viewBox="0 0 16 16"><circle cx="8" cy="8" r="8" fill="#f3e600"/><path d="M4.5 8.2l2.4 2.3 4.6-4.7" fill="none" stroke="#1f2566" stroke-width="1.8"/></svg>Offices</li>
      <li><svg class="tick" viewBox="0 0 16 16"><circle cx="8" cy="8" r="8" fill="#f3e600"/><path d="M4.5 8.2l2.4 2.3 4.6-4.7" fill="none" stroke="#1f2566" stroke-width="1.8"/></svg>Floor Maintenance</li>
      <li><svg class="tick" viewBox="0 0 16 16"><circle cx="8" cy="8" r="8" fill="#f3e600"/><path d="M4.5 8.2l2.4 2.3 4.6-4.7" fill="none" stroke="#1f2566" stroke-width="1.8"/></svg>Carpet Cleaning</li>
      <li><svg class="tick" viewBox="0 0 16 16"><circle cx="8" cy="8" r="8" fill="#f3e600"/><path d="M4.5 8.2l2.4 2.3 4.6-4.7" fill="none" stroke="#1f2566" stroke-width="1.8"/></svg>Move-Ins</li>
      <li><svg class="tick" viewBox="0 0 16 16"><circle cx="8" cy="8" r="8" fill="#f3e600"/><path d="M4.5 8.2l2.4 2.3 4.6-4.7" fill="none" stroke="#1f2566" stroke-width="1.8"/></svg>Move-Outs</li>
      <li><svg class="tick" viewBox="0 0 16 16"><circle cx="8" cy="8" r="8" fill="#f3e600"/><path d="M4.5 8.2l2.4 2.3 4.6-4.7" fill="none" stroke="#1f2566" stroke-width="1.8"/></svg>Constructions Clean- Ups</li>
      <li><svg class="tick" viewBox="0 0 16 16"><circle cx="8" cy="8" r="8" fill="#f3e600"/><path d="M4.5 8.2l2.4 2.3 4.6-4.7" fill="none" stroke="#1f2566" stroke-width="1.8"/></svg>Estate Cleane- Outs</li>
    </ul>
  </section>

  <div class="column-divider"></div>

  <section class="service-list service-list--residential">
    <h2 class="service-title">RESIDENTIAL</h2>
    <ul>
      <li><svg class="tick" viewBox="0 0 16 16"><circle cx="8" cy="8" r="8" fill="#f3e600"/><path d="M4.5 8.2l2.4 2.3 4.6-4.7" fill="none" stroke="#1f2566" stroke-width="1.8"/></svg>House Cleaning</li>
      <li><svg class="tick" viewBox="0 0 16 16"><circle cx="8" cy="8" r="8" fill="#f3e600"/><path d="M4.5 8.2l2.4 2.3 4.6-4.7" fill="none" stroke="#1f2566" stroke-width="1.8"/></svg>Before and After Party</li>
      <li><svg class="tick" viewBox="0 0 16 16"><circle cx="8" cy="8" r="8" fill="#f3e600"/><path d="M4.5 8.2l2.4 2.3 4.6-4.7" fill="none" stroke="#1f2566" stroke-width="1.8"/></svg>Move- Ins</li>
      <li><svg class="tick" viewBox="0 0 16 16"><circle cx="8" cy="8" r="8" fill="#f3e600"/><path d="M4.5 8.2l2.4 2.3 4.6-4.7" fill="none" stroke="#1f2566" stroke-width="1.8"/></svg>Move- Outs</li>
      <li><svg class="tick" viewBox="0 0 16 16"><circle cx="8" cy="8" r="8" fill="#f3e600"/><path d="M4.5 8.2l2.4 2.3 4.6-4.7" fill="none" stroke="#1f2566" stroke-width="1.8"/></svg>Holiday Cleaning</li>
      <li><svg class="tick" viewBox="0 0 16 16"><circle cx="8" cy="8" r="8" fill="#f3e600"/><path d="M4.5 8.2l2.4 2.3 4.6-4.7" fill="none" stroke="#1f2566" stroke-width="1.8"/></svg>Seasonal Cleaning</li>
      <li><svg class="tick" viewBox="0 0 16 16"><circle cx="8" cy="8" r="8" fill="#f3e600"/><path d="M4.5 8.2l2.4 2.3 4.6-4.7" fill="none" stroke="#1f2566" stroke-width="1.8"/></svg>Carpet Cleaning</li>
      <li><svg class="tick" viewBox="0 0 16 16"><circle cx="8" cy="8" r="8" fill="#f3e600"/><path d="M4.5 8.2l2.4 2.3 4.6-4.7" fill="none" stroke="#1f2566" stroke-width="1.8"/></svg>Deodorizing and Sanitizing</li>
    </ul>
  </section>

  <aside class="info-panel">
    <p class="info-note">We adhere to ALL NVB guidelines for<br>both residential and commercial cleaning.</p>
    <p class="info-goal">Infection Control is our ultimate goal.</p>
    <div class="credential"><span class="credential-pill">UMRE trained</span><span class="credential-rule"></span></div>
    <p class="info-bio">Owned and operated by a licensed BSN Registered Nurse specially trained in Infection Control Prevention with over 25 years experience. Over two decades in Ambulatory Surgery Center Administration, Director of Nursing and Infection Control Prevention ad Consulting.</p>
    <p class="call-out">CALL US TO FIND OUT HOW YOU CAN SAVE MONEY THIS MONTH!</p>
    <div class="phone">
      <svg class="phone-icon" viewBox="0 0 34 34" aria-hidden="true">
        <path d="M9 4c1.5-1 3-.6 3.8.8l2.6 4.6c.7 1.3.3 2.6-.8 3.4l-2 1.4c1.3 3 3.8 5.6 6.9 7l1.4-2c.8-1.1 2.2-1.5 3.4-.8l4.6 2.6c1.4.8 1.8 2.4.8 3.8l-1.6 2.2c-1.2 1.7-3.4 2.4-5.4 1.7C14.3 26.6 7.4 19.7 5.3 11.3 4.8 9.4 5.5 7.3 7 6z" fill="#151515"/>
        <path d="M20 5a10 10 0 0 1 9 9M19.5 10a5 5 0 0 1 4.5 4.5" fill="none" stroke="#151515" stroke-width="2.2" stroke-linecap="round"/>
      </svg>
      <span class="phone-number">(415)555 0148</span>
    </div>
  </aside>
</main>
</body>
</html>
```